Compelling Home Page for Clip Harbor Partners

We are a Video SEO specialist that get websites on top of the front page of Zentrova and FlickBarn with video thumbprints that generate great traffic. Video SEO is all we do

see what we're offering at a salespage www.plumfieldreels.example. However, please omit "guarantee"

he home page should introduce our company as a premier company for helping brands get their videos on the front page of zentrova and high up in flickbarn. Should incorporate video "thumbnails" as part of the design. These could be the "triangular click buttons" or little video screens you see as "thumbnails" Needs a prominent place for a video about videoSEO. on Left side of page towards the top.

Needs buttons across the top for other pages. See www.brastonclips.example for frame of reference we want to be better than them.

Must incorporate our logo. We'd like to see the logo on dark background as well as white background.

Simple but with bright and vibrant highlights that look sophisticated, cutting edge and accountable. Shows credentials. Links with examples of thumbnails that are on the front page

We want to beat www.brastonclips.example check it out for point of reference

Target Market(s)

large corporations who have videos already and want to get better traction. Marlow 500. Advertising Agencies for Marlow 500's

Requirements
Must have
• Incorporate our logo. clean, easy to read

```html
<!DOCTYPE html>
<html lang="en">
<head>
<meta charset="utf-8">
<title>Clip Harbor Partners – First Page Video Listings</title>
<link href="https://fonts.googleapis.com/css2?family=Bebas+Neue&family=Open+Sans:ital,wght@0,300;0,400;0,600;0,700;1,400&display=swap" rel="stylesheet">
<style>
:root{
  --dark:#2d2d2d;
  --dark-2:#383838;
  --white:#ffffff;
  --grey-text:#d9d9d9;
  --blue-link:#27b3ea;
  --yellow:#f5c518;
  --mist:#d3dfe0;
  --strip:#e5e9e9;
  --ink:#333;
  --footer-link:#666;
  --panel-frame:#cfe6ef;
  --rule:#777;
}
*{box-sizing:border-box;margin:0;padding:0}
html,body{width:1133px;height:1200px;overflow:hidden}
body{position:relative;font-family:"Open Sans",Arial,sans-serif;background:var(--strip);color:var(--ink)}
.abs{position:absolute}
.display{font-family:"Bebas Neue",Impact,sans-serif;font-weight:400;letter-spacing:-.5px}

.hero{left:0;top:0;width:1133px;height:574px;background:radial-gradient(ellipse at 62% 30%,var(--dark-2),var(--dark) 70%)}
.brand{left:125px;top:30px;display:flex;align-items:center;gap:10px;color:var(--white);font-size:26px;font-weight:300}
.brand-dot{width:40px;height:40px;border-radius:50%;background:var(--yellow)}
.main-nav{left:571px;top:36px;display:flex;gap:36px;font-size:27px;color:var(--white)}
.main-nav .current{color:var(--blue-link)}
.social{left:944px;top:40px;display:flex;gap:10px;font-size:11px;color:var(--grey-text);font-weight:600}
.social span{display:flex;align-items:center;gap:4px}
.social i{width:12px;height:12px;border-radius:50%;background:var(--blue-link);display:inline-block}

.headline{left:123px;top:102px;font-size:52px;line-height:56px;color:var(--white)}
.quote{left:123px;width:378px;text-align:center;font-size:12.3px;line-height:15px;color:var(--grey-text);font-style:italic}
.quote .who{display:block;text-align:right;font-style:normal;font-weight:600;color:var(--white);margin-top:2px}
.quote a{color:var(--blue-link);font-weight:400;text-decoration:underline}
.rule{left:123px;width:378px;height:1px;background:var(--rule)}

.results-frame{left:568px;top:105px;width:449px;height:281px;background:var(--panel-frame);border-radius:14px;padding:8px 0 8px 8px}
.results-shot{width:100%;height:100%;border-radius:8px 0 0 8px;background:linear-gradient(180deg,#ffffff 0%,#f6f3f8 40%,#ffffff 100%)}

.tagline{left:150px;top:418px;width:300px;text-align:center;font-size:58px;line-height:52px;color:var(--white)}
.tagline em{font-style:normal;color:var(--yellow)}
.pitch{left:579px;top:420px;width:440px;font-size:12px;line-height:15px;color:var(--white)}
.pitch strong{display:block;font-size:17px;line-height:20px;font-weight:600}

.band{left:0;top:574px;width:1133px;height:361px;background:var(--mist);border-bottom:2px solid #b9c6c7}
.col-title{font-size:40px;line-height:44px;color:#333}
.copy{font-size:12.5px;line-height:15px;color:#333}
.copy p{margin-bottom:16px}
.copy h3{font-size:14.5px;line-height:18px;font-weight:700;color:#111;margin-bottom:12px}
.order{left:456px;top:533px}
.video{left:417px;top:697px;width:300px;height:186px;border:3px solid #fff;border-radius:4px;background:linear-gradient(135deg,#2a84c0,#0d4f86)}
.play{left:537px;top:760px;width:60px;height:60px;border-radius:50%;background:rgba(40,60,80,.55)}

.partners{left:117px;top:988px;width:890px;display:flex;justify-content:space-between;align-items:center}
.partner{font-size:18px;font-weight:700;color:#555}
.footer-nav{left:123px;top:1084px;font-size:21px;color:var(--footer-link)}
.footer-nav span{margin:0 9px}
.legal{right:126px;top:1123px;text-align:right;font-size:12px;line-height:14px;color:#555}
</style>
</head>
<body>
<section class="hero abs">
  <div class="brand abs"><span class="brand-dot"></span>Clip Harbor Partners</div>
  <nav class="main-nav abs display"><span>ORDER</span><span>REASONS</span><span class="current">ABOUT US</span></nav>
  <div class="social abs"><span><i></i>Chirply</span><span><i></i>Friendora</span></div>

  <h1 class="headline abs display">FIRST PAGE VIDEO LISTINGS</h1>

  <blockquote class="quote abs" style="top:184px">"We were targeting a keyword with 28,600,000 competing pages in an extremely competitive market and the video was showing in position 4 within 2 weeks of being uploaded."
    <span class="who">Dale Morrow, <a>clearrecordcheck.example</a></span></blockquote>
  <div class="rule abs" style="top:267px"></div>
  <blockquote class="quote abs" style="top:288px">"Exceeded our expectations by a mile. We not only have a picture video listing on the first page of Zentrova we also now occupy 6 out of 7 of the first places in Zentrova. [...] just do it before they get too busy."
    <span class="who">Alan Pettigrew, <a>voltwiring.example</a></span></blockquote>
  <div class="rule abs" style="top:390px"></div>

  <div class="results-frame abs">
    <div class="results-shot" role="img" aria-label="Search results page showing the client's video thumbnail listed on the first page"></div>
  </div>

  <h2 class="tagline abs display">WE DO IT <em>ALL</em><br>FOR YOU!</h2>
  <div class="pitch abs">
    <p>No matter what you sell or what your company size, VIDEO MARKETING is very likely your best opportunity to dramatically increase online sales this year.</p>
    <p style="margin-top:13px">You'll have First page listings on Zentrova for the Keywords of Your Choice...</p>
    <strong>For More Traffic, Leads, and Sales to Your Site!</strong>
  </div>
</section>

<section class="band abs">
  <h2 class="col-title display abs" style="left:123px;top:12px">BE FIRST ON ZENTROVA</h2>
  <div class="copy abs" style="left:123px;top:64px;width:290px">
    <p>You'll get first page Zentrova video listings or you get your money back! We work with ALL types of products and services at reasonable rates...</p>
    <p>We help entrepreneurs, small businesses, and even large brands (affiliate marketers too)...</p>
    <p>Plus, WE can produce the videos for you--OR--work with video's YOU provide us...</p>
  </div>
  <h2 class="col-title display abs" style="left:725px;top:12px">EXPAND TRAFFIC &amp; SALES</h2>
  <div class="copy abs" style="left:727px;top:64px;width:285px">
    <p>VIDEO is Fast Becoming THE Preferred Method to Expand Your TRAFFIC and SALES on the Internet for TWO Important Reasons:</p>
    <h3>#1 There is MUCH Less Competition in the VIDEO Keyword Space (even in brutally competitive markets)</h3>
    <p>Video can literally be more than 418,000 percent less competitive!</p>
    <p>(There's 4,185 times less competition for wedding dresses above, for example)</p>
  </div>
</section>

<svg class="order abs" width="222" height="140" viewBox="0 0 222 140" aria-label="Order now – free video SEO consult">
  <path d="M4 0 H218 Q222 0 222 4 V80 L111 138 L0 80 V4 Q0 0 4 0Z" fill="#c8141b" stroke="#9b0e13" stroke-width="2"/>
  <text x="111" y="56" text-anchor="middle" font-family="Bebas Neue, Impact, sans-serif" font-size="52" fill="#fff">ORDER NOW</text>
  <text x="111" y="79" text-anchor="middle" font-family="Open Sans, Arial, sans-serif" font-size="15" font-weight="700" fill="#f3d0d0">Free Video SEO Consult</text>
  <line x1="80" y1="88" x2="142" y2="88" stroke="#e65a5a"/>
  <polygon points="111,102 115,112 125,112 117,118 120,128 111,122 102,128 105,118 97,112 107,112" fill="#fff"/>
</svg>

<div class="video abs" role="img" aria-label="Presenter introducing the video SEO service"></div>
<div class="play abs"></div>
<svg class="abs" style="left:555px;top:776px" width="28" height="28" viewBox="0 0 28 28"><polygon points="4,2 26,14 4,26" fill="#2b3440" opacity=".7"/></svg>

<div class="partners abs">
  <span class="partner">Crestel</span>
  <span class="partner">Grill Baron</span>
  <span class="partner">Lumaro</span>
  <span class="partner">Swirlmaster</span>
  <span class="partner">PayCircle</span>
  <span class="partner">Meridian Pay</span>
</div>

<nav class="footer-nav abs display">DISCLAIMER &amp; TOU<span>|</span>PRIVACY<span>|</span>DISCLOSURE<span>|</span>LEGAL<span>|</span>SUPPORT<span>|</span>HOME</nav>
<div class="legal abs">© Clip Harbor Partners, LLC. - All Rights Reserved<br>Trademarks on this page are the property of their respective owners.</div>
</body>
</html>
```